Fernvale Pharmacy opening

We want to have a double sided 5.5"x8.5" flyer for a new Pharmacy opening in a well known strip mall in the neighborhood and we are planning to mail it to neighbors homes.

Want to put the outside pharmacy picture on the main side of the flyer and a coupon with 25% off towards an OTC product on the back in addition to the info below (preferably in a sort of bulletin points not a list (something like the 2 examples attached).

Colors to be red like the exterior sign and blue like the interior wall paint:

Front side should have:
Fernvale pharmacy
Your locally owned and operated pharmacy around the corner.
317-4082 Tarrow rd.
Brisket hollow plaza
T. 604 827 5530 (call or text)
F. 604-827-5532

Free prescription delivery
Text us for refills
Specialized compounding
Customized compression stockings

The back side should have:

Do you forget taking your medications! We offer multiple compliance packaging options at no additional cost.
Had shingles before or worried to have it? travelling soon? check our vaccinations options!
Suffering side effects? We are experienced to check your medications interactions & different coverage options.
Hard time monitoring your blood pressure? Trying to stop smoking? we can always help.

FEELING BETTER STARTS HERE

```html
<!DOCTYPE html>
<html lang="en">
<head>
<meta charset="utf-8">
<title>Fernvale Pharmacy – Grand Opening Flyer</title>
<link href="https://fonts.googleapis.com/css2?family=Montserrat:wght@500;600;700;800&display=swap" rel="stylesheet">
<style>
:root{
  --red:#e8141b;
  --red-dark:#c10d12;
  --blue:#1d5fb4;
  --blue-deep:#154a93;
  --blue-light:#2f7fd6;
  --grey-band:#e4e4e4;
  --grey-row:#c2c2c2;
  --ink:#1f1f1f;
  --white:#ffffff;
  --stage:#3b4856;
  --page:#ffffff;
}
*{margin:0;padding:0;box-sizing:border-box}
html,body{width:1200px;height:3872px;overflow:hidden}
body{background:var(--page);font-family:"Montserrat",Arial,sans-serif;position:relative;color:var(--ink)}

.stage{position:absolute;left:0;top:0;width:1200px;height:1080px;background:linear-gradient(180deg,#465566,var(--stage))}
.stage-slot{position:absolute;top:190px;width:753px;height:1162px;transform:scale(.6);transform-origin:0 0;box-shadow:0 20px 50px rgba(0,0,0,.45)}
.stage-slot.front{left:128px}
.stage-slot.back{left:620px}

.sheet{position:absolute;left:222px;width:753px;height:1162px;box-shadow:0 10px 40px rgba(0,0,0,.18)}
.sheet.front{top:1204px}
.sheet.back{top:2494px}

.flyer{position:relative;width:753px;height:1162px;background:var(--white);overflow:hidden}
.abs{position:absolute}

/* front */
.hero{left:0;top:0;width:753px;height:435px;background:var(--blue)}
.hero svg{position:absolute;left:0;top:0}
.brand-mark{left:88px;top:40px;width:96px;height:96px;border-radius:50%;background:var(--red)}
.brand-name{left:33px;top:208px;color:var(--white);font-weight:700;font-size:36px;line-height:36px;letter-spacing:.5px;text-transform:uppercase}
.headline{left:31px;top:296px;color:var(--white);font-weight:800;font-size:82px;line-height:66px;letter-spacing:1px}
.tagline-band{left:0;top:435px;width:753px;height:142px;background:var(--grey-band)}
.tagline{left:33px;top:462px;width:405px;color:var(--red);font-weight:800;text-transform:uppercase;line-height:1}
.tagline .l1{display:block;font-size:45px;letter-spacing:.3px}
.tagline .l2{display:block;font-size:28px;margin-top:2px;letter-spacing:.3px}
.tagline .l3{display:block;font-size:19px;font-weight:700;margin-top:4px;letter-spacing:.2px}
.meds-art{left:452px;top:405px;width:290px;height:190px;border-radius:18px;background:linear-gradient(135deg,#f2c05a,#e9e2d4 45%,#c7472e);opacity:.9}

.service{display:flex;align-items:center;gap:22px}
.service-icon{width:86px;height:86px;border-radius:50%;border:2px dashed var(--blue);display:flex;align-items:center;justify-content:center;flex:none}
.service-icon span{width:66px;height:66px;border-radius:50%;background:var(--blue);display:flex;align-items:center;justify-content:center}
.service p{font-weight:600;font-size:22px;line-height:27px;color:var(--ink)}

.contact-frame{left:0;top:838px;width:753px;height:240px;background:var(--blue);border-radius:14px 0 0 14px}
.contact-box{left:15px;top:857px;width:560px;height:200px;background:var(--red);border-radius:12px}
.contact-title{left:42px;top:880px;color:var(--white);font-weight:700;font-size:33px}
.contact-lines{left:42px;top:932px;color:var(--white);font-weight:700;font-size:23px;line-height:28px;list-style:none}
.contact-lines li{display:flex;align-items:flex-start;gap:14px}
.contact-lines svg{flex:none;margin-top:4px}
.pharmacist-art{left:400px;top:790px;width:353px;height:372px;background:linear-gradient(160deg,#4a9a6a 0%,#e9edf1 45%,#f6f6f6 100%);border-radius:40px 0 0 0}

/* back */
.back-hero{left:0;top:0}
.issue{left:0;width:753px;height:100px;background:var(--grey-row)}
.issue svg{position:absolute;left:0;top:0}
.issue .q{position:absolute;left:48px;top:0;width:310px;height:86px;display:flex;align-items:center;color:var(--white);font-weight:700;font-size:20px;line-height:25px}
.issue .a{position:absolute;left:393px;top:0;width:345px;height:100px;display:flex;align-items:center;color:var(--ink);font-weight:600;font-size:20px;line-height:21px}
.coupon-frame{left:60px;top:930px;width:630px;height:173px;border:3px dashed #222;border-radius:12px}
.coupon{left:96px;top:952px;width:556px;height:127px;background:var(--blue);border-radius:14px;overflow:hidden}
.coupon-value{left:0;top:0;width:181px;height:127px;background:var(--red);color:var(--white);font-weight:800;font-size:68px;display:flex;align-items:center;justify-content:center}
.coupon-text{left:200px;top:20px;color:var(--white);font-weight:800;font-size:33px;line-height:38px}
.foot-band{left:0;top:1118px}
</style>
</head>
<body>

<div class="stage">
  <div class="stage-slot front">
    <div class="flyer">
      <div class="abs hero">
        <svg width="753" height="435" viewBox="0 0 753 435">
          <path role="img" aria-label="Photo of the pharmacy interior with stocked shelves" d="M290,0 H753 V372 C620,420 430,360 350,210 C305,130 285,60 290,0Z" fill="#7c8696"/>
          <path d="M330,250 C430,420 610,420 753,355 V405 C600,455 420,420 330,250Z" fill="#e8141b"/>
          <path d="M350,300 C460,430 630,440 753,405 V435 H520 C440,410 385,360 350,300Z" fill="#154a93"/>
        </svg>
      </div>
      <div class="abs brand-mark"></div>
      <div class="abs brand-name">Fernvale<br>Pharmacy</div>
      <div class="abs headline">GRAND<br>OPENING</div>
      <div class="abs tagline-band"></div>
      <div class="abs tagline"><span class="l1">Your locally</span><span class="l2">owned and operated</span><span class="l3">pharmacy around the corner</span></div>
      <div class="abs meds-art" role="img" aria-label="Illustration of medicine bottles and pills"></div>
      <div class="abs contact-frame"></div>
      <div class="abs contact-box"></div>
      <div class="abs pharmacist-art" role="img" aria-label="Photo of a smiling pharmacist with a medical kit"></div>
      <div class="abs contact-title">Call or text</div>
    </div>
  </div>
  <div class="stage-slot back">
    <div class="flyer">
      <svg class="abs back-hero" width="753" height="468" viewBox="0 0 753 468">
        <rect role="img" aria-label="Photo of a pharmacist in a white coat" width="753" height="468" fill="#1d5fb4"/>
        <path role="img" aria-label="Photo of pharmacy shelves" d="M0,0 H420 C405,190 300,310 0,320Z" fill="#8c8f95"/>
        <path d="M0,320 C300,310 405,190 420,0 H440 C430,220 320,350 0,360Z" fill="#e8141b"/>
      </svg>
    </div>
  </div>
</div>

<!-- Front -->
<section class="sheet front" aria-label="Flyer front">
  <div class="flyer">
    <div class="abs hero">
      <svg width="753" height="435" viewBox="0 0 753 435">
        <path role="img" aria-label="Photo of the pharmacy interior with stocked shelves" d="M290,0 H753 V372 C620,420 430,360 350,210 C305,130 285,60 290,0Z" fill="#7c8696"/>
        <path d="M330,250 C430,420 610,420 753,355 V405 C600,455 420,420 330,250Z" fill="#e8141b"/>
        <path d="M350,300 C460,430 630,440 753,405 V435 H520 C440,410 385,360 350,300Z" fill="#154a93"/>
      </svg>
    </div>
    <div class="abs brand-mark"></div>
    <div class="abs brand-name">Fernvale<br>Pharmacy</div>
    <h1 class="abs headline">GRAND<br>OPENING</h1>

    <div class="abs tagline-band"></div>
    <p class="abs tagline"><span class="l1">Your locally</span><span class="l2">owned and operated</span><span class="l3">pharmacy around the corner</span></p>
    <div class="abs meds-art" role="img" aria-label="Illustration of medicine bottles and pills"></div>

    <div class="abs service" style="left:35px;top:597px">
      <div class="service-icon"><span><svg width="34" height="34" viewBox="0 0 34 34"><rect x="3" y="12" width="18" height="12" rx="2" fill="#fff"/><circle cx="8" cy="27" r="4" fill="#fff"/><circle cx="26" cy="27" r="4" fill="#fff"/><circle cx="23" cy="6" r="4" fill="#fff"/></svg></span></div>
      <p>Free prescription<br>delivery</p>
    </div>
    <div class="abs service" style="left:395px;top:597px">
      <div class="service-icon"><span><svg width="34" height="34" viewBox="0 0 34 34"><rect x="9" y="3" width="16" height="5" rx="1" fill="#fff"/><rect x="7" y="9" width="20" height="22" rx="4" fill="#fff"/><path d="M17 14v10M12 19h10" stroke="#1d5fb4" stroke-width="3"/></svg></span></div>
      <p>Text us for<br>refills</p>
    </div>
    <div class="abs service" style="left:35px;top:699px">
      <div class="service-icon"><span><svg width="34" height="34" viewBox="0 0 34 34"><path d="M6 16h22l-3 12H9z" fill="#fff"/><rect x="18" y="3" width="4" height="14" rx="2" transform="rotate(30 20 10)" fill="#fff"/></svg></span></div>
      <p>Specialized<br>compounding</p>
    </div>
    <div class="abs service" style="left:395px;top:699px">
      <div class="service-icon"><span><svg width="34" height="34" viewBox="0 0 34 34"><rect x="4" y="7" width="26" height="20" rx="2" fill="#fff"/><path d="M9 12v10M14 12v10M20 12v10M25 12v10" stroke="#1d5fb4" stroke-width="3"/></svg></span></div>
      <p>Customized<br>compression<br>stockings</p>
    </div>

    <div class="abs contact-frame"></div>
    <div class="abs contact-box"></div>
    <div class="abs pharmacist-art" role="img" aria-label="Photo of a smiling pharmacist with a medical kit"></div>
    <h2 class="abs contact-title">Call or text</h2>
    <ul class="abs contact-lines">
      <li><svg width="16" height="18" viewBox="0 0 16 18"><path d="M3 1l3 4-2 2c1 3 3 5 6 6l2-2 4 3-2 3C7 17 0 10 1 3z" fill="#fff"/></svg>604 827 5530</li>
      <li><svg width="16" height="18" viewBox="0 0 16 18"><path d="M3 1l3 4-2 2c1 3 3 5 6 6l2-2 4 3-2 3C7 17 0 10 1 3z" fill="#fff"/></svg>604-827-5532</li>
      <li style="margin-top:4px"><svg width="16" height="20" viewBox="0 0 16 20"><path d="M8 1a6 6 0 0 1 6 6c0 4-6 10-6 10S2 11 2 7a6 6 0 0 1 6-6z" fill="none" stroke="#fff" stroke-width="2.4"/><circle cx="8" cy="7" r="2" fill="#fff"/><path d="M1 19h14" stroke="#fff" stroke-width="2"/></svg><span>317-4082 Tarrow<br>rd. Brisket hollow plaza</span></li>
    </ul>
  </div>
</section>

<!-- Back -->
<section class="sheet back" aria-label="Flyer back">
  <div class="flyer">
    <svg class="abs back-hero" width="753" height="468" viewBox="0 0 753 468">
      <defs><linearGradient id="staffTone" x1="0" y1="0" x2="1" y2="1"><stop offset="0" stop-color="#2f7fd6"/><stop offset="1" stop-color="#1a55a3"/></linearGradient></defs>
      <rect role="img" aria-label="Photo of a pharmacist in a white coat with a stethoscope" width="753" height="468" fill="url(#staffTone)"/>
      <path role="img" aria-label="Photo of pharmacy shelves with products" d="M0,0 H420 C405,190 300,310 0,320Z" fill="#8c8f95"/>
      <path d="M0,320 C300,310 405,190 420,0 H440 C430,220 320,350 0,360Z" fill="#e8141b"/>
      <path d="M0,360 C320,350 430,220 440,0 H452 C442,230 330,365 0,375Z" fill="#154a93"/>
    </svg>

    <div class="abs issue" style="top:478px">
      <svg width="380" height="100" viewBox="0 0 380 100"><path d="M0,6 H355 L375,48 L355,90 H0Z" fill="#154a93"/><path d="M0,0 H350 L372,43 L350,86 H0Z" fill="#e8141b"/></svg>
      <p class="q">Do you forget taking your medications!</p>
      <p class="a">We offer multiple compliance packaging options at no additional cost.</p>
    </div>
    <div class="abs issue" style="top:580px">
      <svg width="380" height="100" viewBox="0 0 380 100"><path d="M0,6 H355 L375,48 L355,90 H0Z" fill="#154a93"/><path d="M0,0 H350 L372,43 L350,86 H0Z" fill="#e8141b"/></svg>
      <p class="q">Had shingles before or worried to have it? travelling soon?</p>
      <p class="a">Check our vaccinations options!</p>
    </div>
    <div class="abs issue" style="top:690px">
      <svg width="380" height="100" viewBox="0 0 380 100"><path d="M0,6 H355 L375,48 L355,90 H0Z" fill="#154a93"/><path d="M0,0 H350 L372,43 L350,86 H0Z" fill="#e8141b"/></svg>
      <p class="q">Suffering side effects?</p>
      <p class="a">We are experienced to check your medications interactions &amp; different coverage options.</p>
    </div>
    <div class="abs issue" style="top:805px">
      <svg width="380" height="100" viewBox="0 0 380 100"><path d="M0,6 H355 L375,48 L355,90 H0Z" fill="#154a93"/><path d="M0,0 H350 L372,43 L350,86 H0Z" fill="#e8141b"/></svg>
      <p class="q">Hard time monitoring your blood pressure? Trying to stop smoking?</p>
      <p class="a">We can always help.</p>
    </div>

    <div class="abs coupon-frame"></div>
    <div class="abs coupon">
      <div class="abs coupon-value">25%</div>
      <p class="abs coupon-text">OFF TOWARDS<br>AN OTC PRODUCT</p>
    </div>

    <svg class="abs foot-band" width="753" height="44" viewBox="0 0 753 44">
      <path d="M0,0 H405 L385,44 H0Z" fill="#1d5fb4"/>
      <path d="M415,44 L435,0 H753 V44Z" fill="#e8141b"/>
    </svg>
  </div>
</section>

</body>
</html>
```